Tavo's Spice Blend Dry Roasted and Freshly Ground Spices to create the Authentic and Aromatic Maur

I need a packaging design for a new company based in Kent called Tavo's Spice Blend. the size of the packaging will be for a 250gm bag.

I would like bright colours so that it can stand out from out the other products on a super market shelf

The packaging must have the list of ingredients on the back;

I.e. Ingredients;
Cumin
Coriander
Dried Red Chili
Cinnamon
Cloves
Cardamon
Black Peppercorn
Rice

Reason: Not enough designed to choose from. Tavo's Spice Blend, Dry Roasted and Freshly Ground Spices to create the Authentic and Aromatic flavour Please also add Turmeric to the ingredient list Thank you Bronna Castell

```html
<!DOCTYPE html>
<html lang="en">
<head>
<meta charset="utf-8">
<title>Tavo's Spice Blend – 250g Pack</title>
<link rel="stylesheet" href="https://fonts.googleapis.com/css2?family=Architects+Daughter&family=Cabin+Sketch:wght@700&display=swap">
<style>
  :root {
    --page: #ffffff;
    --sun-yellow: #f6ba10;
    --deep-saffron: #f3a30b;
    --halo-light: #f7c522;
    --halo-deep: #f1a70d;
    --cream: #f5e6ae;
    --brand-yellow: #f3bb14;
    --ink: #1e1a14;
    --white: #ffffff;
  }
  * { margin: 0; padding: 0; box-sizing: border-box; }
  html, body {
    width: 1200px; height: 607px; overflow: hidden;
    background: var(--page);
  }
  .canvas { position: relative; width: 1200px; height: 607px; }
  .pack-face {
    position: absolute; top: 10px;
    width: 607px; height: 607px;
    transform: scale(0.9638); transform-origin: top left;
    overflow: hidden;
  }
  .pack-front { left: 8px; }
  .pack-back { left: 607px; }
  .face-bg { position: absolute; inset: 0; width: 607px; height: 607px; }

  .brand-name {
    position: absolute; left: 0; width: 607px; top: 95px;
    text-align: center;
    font-family: "Cabin Sketch", "Arial Black", sans-serif;
    font-weight: 700; font-size: 122px; line-height: 1;
    letter-spacing: 4px;
    color: var(--brand-yellow);
  }
  .product-name {
    position: absolute; left: 0; width: 607px; top: 246px;
    text-align: center;
    font-family: "Architects Daughter", cursive;
    font-size: 27px; letter-spacing: 10px;
    color: var(--ink);
  }
  .net-weight {
    position: absolute; left: 0; width: 607px; top: 528px;
    text-align: center;
    font-family: "Architects Daughter", cursive;
    font-size: 36px; letter-spacing: 14px;
    color: var(--white);
  }
  .ingredients-title {
    position: absolute; left: 0; width: 585px; top: 105px;
    text-align: center;
    font-family: "Architects Daughter", cursive;
    font-size: 36px; letter-spacing: 7px;
    color: var(--white);
  }
  .ingredients-list {
    position: absolute; left: 0; width: 607px; top: 306px;
    list-style: none; text-align: center;
    font-family: "Architects Daughter", cursive;
    font-size: 20px; line-height: 29.6px; letter-spacing: 2px;
    color: var(--ink);
  }
</style>
</head>
<body>
<main class="canvas">
  <section class="pack-face pack-front" aria-label="Front of pack">
    <svg class="face-bg" viewBox="0 0 607 607" aria-hidden="true">
      <rect width="607" height="607" fill="var(--sun-yellow)"/>
      <rect y="322" width="607" height="285" fill="var(--deep-saffron)"/>
      <circle cx="303" cy="161" r="290" fill="var(--halo-light)"/>
      <circle cx="303" cy="161" r="262" fill="var(--cream)"/>
    </svg>
    <h1 class="brand-name">TAVO'S</h1>
    <p class="product-name">SPICE BLEND</p>
    <p class="net-weight">250g</p>
  </section>

  <section class="pack-face pack-back" aria-label="Back of pack">
    <svg class="face-bg" viewBox="0 0 607 607" aria-hidden="true">
      <rect width="607" height="607" fill="var(--sun-yellow)"/>
      <rect y="330" width="607" height="277" fill="var(--deep-saffron)"/>
      <circle cx="303" cy="478" r="312" fill="var(--halo-deep)"/>
      <circle cx="303" cy="478" r="292" fill="var(--cream)"/>
    </svg>
    <h2 class="ingredients-title">Ingredients:</h2>
    <ul class="ingredients-list">
      <li>CUMIN</li>
      <li>CORIANDER</li>
      <li>DRIED RED CHILI</li>
      <li>CINNAMON</li>
      <li>CLOVES</li>
      <li>CARDAMON</li>
      <li>BLACK PEPPERCORN</li>
      <li>RICE</li>
    </ul>
  </section>
</main>
</body>
</html>
```